Brightmere Glowworks - Two Pages of Information and Pictures

We need a two page summary of the Service Offerings of Brightmere Glowworks - a company that installs LED Lighting. We've written the copy and picked images and chart that we like and have laid it out a word document.

We're looking for someone to design a more professional page layout than the generic Word Template. Please do not feel the current layout is suggested. It is only laid out this way because Word had that template. Be as creative as you want.

We would like the images and text to be in the same order that it is in now.

We're also in a rush so speed is appreciated. THANK YOU !!

Target Market(s)

Corporate Offices in New York

Industry/Entity Type

Lighting Fixture

Colors
85cae6
87cfc7
9bcb3c
3377b5

Requirements
Must have
• Must include two pages of the copy and images written and provided in the word document that was uploaded. Must use the Brightmere colors in the logo.
Nice to have
• An easy to read flow of images and.

```html
<!DOCTYPE html>
<html lang="en">
<head>
<meta charset="utf-8">
<title>Brightmere Glowworks – Making LEDs Beautiful</title>
<link rel="stylesheet" href="https://fonts.googleapis.com/css2?family=Open+Sans:wdth,wght@75..100,300..700&family=Poppins:wght@300&display=swap">
<style>
  :root {
    --paper: #f2f2f2;
    --teal: #87cfc7;
    --blue: #3377b5;
    --green: #9bcb3c;
    --sky: #85cae6;
    --white: #ffffff;
    --body-copy: #eef6dc;
    --brand-ink: #4f8a6a;
  }
  html, body {
    margin: 0;
    padding: 0;
    overflow: hidden;
    background: var(--paper);
  }
  .page {
    position: relative;
    width: 848px;
    height: 1200px;
    overflow: hidden;
    background: var(--paper);
  }
  .page-art {
    position: absolute;
    inset: 0;
    display: block;
  }
  .brand {
    position: absolute;
    left: 30px;
    top: 86px;
    width: 252px;
    display: flex;
    align-items: center;
    justify-content: center;
    gap: 12px;
  }
  .brand-dot {
    width: 26px;
    height: 26px;
    border-radius: 50%;
    background: var(--teal);
    flex: none;
  }
  .brand-name {
    margin: 0;
    font-family: "Poppins", sans-serif;
    font-weight: 300;
    font-size: 29px;
    letter-spacing: 1.5px;
    color: var(--brand-ink);
  }
  .headline {
    position: absolute;
    left: 30px;
    top: 284px;
    margin: 0;
    font-family: "Open Sans", sans-serif;
    font-stretch: 75%;
    font-weight: 700;
    font-size: 80px;
    line-height: 99px;
    letter-spacing: -2px;
    color: var(--white);
  }
  .offer {
    position: absolute;
    left: 33px;
    right: 33px;
    top: 962px;
  }
  .offer-title {
    margin: 0 0 16px;
    text-align: center;
    font-family: "Open Sans", sans-serif;
    font-stretch: 87.5%;
    font-weight: 300;
    font-size: 41px;
    letter-spacing: -0.5px;
    line-height: 1.1;
    color: var(--white);
  }
  .offer-copy {
    margin: 0;
    text-align: justify;
    font-family: "Poppins", sans-serif;
    font-weight: 300;
    font-size: 16.2px;
    line-height: 24.2px;
    color: var(--body-copy);
  }
</style>
</head>
<body>
<main class="page">
  <svg class="page-art" width="848" height="1200" viewBox="0 0 1060 1500">
    <defs>
      <linearGradient id="office-tone" x1="0.2" y1="0" x2="0.7" y2="1">
        <stop offset="0" stop-color="#f6f5f1"/>
        <stop offset="0.35" stop-color="#ebe8e1"/>
        <stop offset="0.6" stop-color="#c9c2b4"/>
        <stop offset="0.78" stop-color="#8a8377"/>
        <stop offset="1" stop-color="#2f2f31"/>
      </linearGradient>
      <linearGradient id="lounge-tone" x1="0" y1="0" x2="0" y2="1">
        <stop offset="0" stop-color="#3d3d3f"/>
        <stop offset="0.14" stop-color="#6b6b6c"/>
        <stop offset="0.3" stop-color="#e2e2e0"/>
        <stop offset="0.55" stop-color="#a9a7a2"/>
        <stop offset="0.75" stop-color="#eeeeec"/>
        <stop offset="1" stop-color="#c6c6c4"/>
      </linearGradient>
      <radialGradient id="pendant-tone" cx="0.55" cy="0.5" r="0.65">
        <stop offset="0" stop-color="#f3d48e"/>
        <stop offset="0.25" stop-color="#b8884c"/>
        <stop offset="0.6" stop-color="#4d3a2b"/>
        <stop offset="1" stop-color="#1f1a17"/>
      </radialGradient>
    </defs>

    <rect x="0" y="0" width="1060" height="1500" fill="var(--paper)"/>
    <rect class="title-band" x="0" y="300" width="1060" height="480" fill="var(--teal)"/>

    <polygon class="photo photo-office" role="img" aria-label="Open-plan office lit by suspended linear LED fixtures"
      points="610,0 1060,0 1060,780 867,780 345,258" fill="url(#office-tone)"/>

    <rect class="photo-frame" x="0" y="780" width="1060" height="390" fill="var(--white)"/>
    <rect class="photo photo-lounge" role="img" aria-label="Office kitchen and lounge with recessed LED downlights"
      x="0" y="780" width="583" height="380" fill="url(#lounge-tone)"/>
    <rect class="photo photo-pendants" role="img" aria-label="Cluster of caged pendant lamps with warm LED filament bulbs"
      x="592" y="780" width="468" height="338" fill="url(#pendant-tone)"/>

    <polygon class="info-band" points="0,1168 592,1168 592,1127 1060,1127 1060,1500 0,1500" fill="var(--green)"/>

    <polygon class="chevron-stripe"
      points="560,0 610,0 345,258 900,815 1060,655 1060,705 900,865 295,258" fill="var(--blue)"/>
  </svg>

  <div class="brand">
    <span class="brand-dot"></span>
    <p class="brand-name">BRIGHTMERE</p>
  </div>

  <h1 class="headline">MAKING<br>LEDS<br>BEAUTIFUL</h1>

  <section class="offer">
    <h2 class="offer-title">NO UPFRONT COST –TURNKEY LEDS</h2>
    <p class="offer-copy">Brightmere Glowworks provides LED lighting as a service – fully implemented and managed LEDs at no upfront cost. Brightmere takes the risk, hassle and capital cost out of adopting LED’s energy saving technology. Brightmere guarantees net-savings for customers on day one, and continues to guarantee savings and performance for the full term of the contract. And the savings add up! A project can be installed 2-4 weeks from kickoff, and projects continue to generate savings for up to 10 years.</p>
  </section>
</main>
</body>
</html>
```